Law firm business card

Information:

Me Miriam Dufresne

website: dufresne-law.ca
email: miriam@dufresne-law.ca
Phone: 514 555-0147
Fax: 514 555-0183

Address:
Dufresne and associates
2719 Belcourt
Montreal, QC
H2K 3M9

Areas of Expertise:
Franchise Agreements, Financing, Acquisition, Real Estate Development, Commercial Agreements and Corporate Law

Target Market(s)

executives, companie managers

Industry/Entity Type

Business

Colors
f78f20
000000

Requirements
Must have
• Must use the logo, the logo is available here:

https://www.filebinder-example.com/sh/qxt8rr2ka41wpe/BBKtm7Lwzve_pQRYdNG_HJcWb

```html
<!DOCTYPE html>
<html lang="en">
<head>
<meta charset="utf-8">
<title>Dufresne &amp; Associates – Business Card</title>
<link rel="stylesheet" href="https://fonts.googleapis.com/css2?family=Open+Sans:wght@400&display=swap">
<style>
  :root {
    --orange: #f78f20;
    --black: #000000;
    --white: #ffffff;
    --ink: #1a1a1a;
    --backdrop: #e6e6e6;
    --font-text: "Open Sans", Arial, sans-serif;
  }
  * { margin: 0; padding: 0; box-sizing: border-box; }
  html, body { width: 1200px; height: 1000px; overflow: hidden; }
  body { background: var(--backdrop); font-family: var(--font-text); }

  .canvas { position: relative; width: 1200px; height: 1000px; }

  .card {
    position: absolute;
    width: 540px;
    height: 309px;
    overflow: hidden;
    box-shadow: 0 6px 18px rgba(0,0,0,0.18);
  }

  /* Contact side */
  .card--details { left: 60px; top: 150px; background: var(--black); }
  .details-panel {
    position: absolute; inset: 0;
    background: var(--orange);
    clip-path: polygon(37% 0, 100% 0, 100% 100%, 72% 100%);
  }
  .contact {
    position: absolute; left: 64%; top: 24px;
    font-size: 12.5px; line-height: 1.25; color: var(--ink);
  }
  .contact p { white-space: nowrap; }
  .address { margin-top: 26px; }
  .holder-name {
    position: absolute; left: 40px; top: 178px;
    font-size: 22px; font-weight: 400; color: var(--orange);
    letter-spacing: 0.3px; white-space: nowrap;
  }
  .expertise {
    position: absolute; left: 40px; top: 228px;
    font-size: 11px; line-height: 1.35; color: var(--white);
  }
  .expertise span { display: block; white-space: nowrap; }

  /* Firm side */
  .card--front { left: 600px; top: 520px; background: var(--orange); }
  .front-edge {
    position: absolute; top: 0; right: 0; width: 9%; height: 100%;
    background: var(--black);
  }
  .name-band {
    position: absolute; left: 0; top: 122px; width: 77%; height: 86px;
    background: var(--white);
    display: flex; align-items: center; padding-left: 48px;
  }
  .firm-name {
    font-size: 22px; font-weight: 400; color: var(--ink);
    white-space: nowrap;
  }
</style>
</head>
<body>
  <main class="canvas">
    <section class="card card--details" aria-label="Business card, contact side">
      <div class="details-panel"></div>
      <div class="contact">
        <p>Website: dufresne-law.ca</p>
        <p>email: miriam@dufresne-law.ca</p>
        <p>Phone: 514 555-0147</p>
        <p>Fax: 514 555-0183</p>
        <div class="address">
          <p>Address:</p>
          <p>Dufresne and associates</p>
          <p>2719 Belcourt</p>
          <p>Montreal, QC</p>
          <p>H2K 3M9</p>
        </div>
      </div>
      <h1 class="holder-name">Miriam Dufresne</h1>
      <p class="expertise">
        <span>Franchise Agreements, Financing,</span>
        <span>Acquisition,Real Estate Development,</span>
        <span>Commercial Agreements and Corporate Law</span>
      </p>
    </section>

    <section class="card card--front" aria-label="Business card, firm side">
      <div class="front-edge"></div>
      <div class="name-band">
        <span class="firm-name">Dufresne &amp; Associates</span>
      </div>
    </section>
  </main>
</body>
</html>
```